Presentation card Venture KELO - Tech Incubator from Perú

We need a Design to promote the incubator of technology Startups.
We are in Perú, we work with a string tech filter and develop enterprenurship competencies in the Startup team.
The card is to facilitators and staff memebers of VentureKELO.
We want a clear, modern, tech and agile Design.

We work to help New enterprises of technology here in Perú, we expect the candidates have a big competencies to Research and develop technological products.

We work using methodologies from QRB, Folmestry, Brakewell and Harrowgate univeesities. Our book base is the disciplina of enterpreneur.

We work events all year using diferent formats: Brightforge, Vorne price, OPRA Model Competition you can use these logros in your Design.

Set the name, role, email, cell phone number, address.

Example:
// Contact info section
Tobías Quiroveda
Swift Modeling Hub Manager
tobias.quiroveda@kelo-example.pe
(511) 999 000 417

// Address info section
VentureKELO
Technology-based business incubator
Av. Los Cedrales 884, Valdora
Lima - Perú
web: venture-kelo-example.org.pe
email: venture@kelo-example.pe
phone number: (511) 3926508 ext. 4418

// (optional)Lema section
Making happy using technology

// Social network section
facebook: venturekelooficial

Target Market(s)

Enterprenurship, CTO, Investors, Companies interested on open innovation services

Industry/Entity Type

Information Technology

Contact Information for Business Card

Name, Role, Email, Cell phone number

Colors

Designer to choose colors to be used in the design.

Requirements
Must have
• Logo forms and colors
Nice to have
• I add pictures of the leaders of incubator
Should not have
• No vertical designs

```html
<!DOCTYPE html>
<html lang="en">
<head>
<meta charset="utf-8">
<title>Venture KELO – Business Card</title>
<link href="https://fonts.googleapis.com/css2?family=Lato:wght@400;700;900&display=swap" rel="stylesheet">
<style>
  :root {
    --stage: #5d5d5f;
    --paper: #ffffff;
    --ink: #222224;
    --crimson: #c0325a;
    --night: #2b2a2c;
    --photo-a: #d9dbe0;
    --photo-b: #2e3548;
  }
  * { margin: 0; padding: 0; box-sizing: border-box; }
  html, body { width: 1200px; height: 802px; overflow: hidden; }
  body {
    background: var(--stage);
    font-family: "Lato", sans-serif;
    position: relative;
  }
  .card {
    position: absolute;
    top: 274px;
    width: 443px;
    height: 265px;
    box-shadow: 0 4px 10px rgba(0,0,0,0.45);
    overflow: hidden;
  }
  .card-front { left: 136px; background: var(--paper); }
  .card-back { left: 624px; background: var(--night); }

  .portrait {
    position: absolute;
    left: 0;
    top: 59px;
    width: 228px;
    height: 197px;
    background: linear-gradient(180deg, var(--photo-a) 0%, #b9a08c 35%, var(--photo-b) 70%);
    border-radius: 90px 90px 0 0;
  }
  .brand-band {
    position: absolute;
    left: 0; right: 0; bottom: 0;
    height: 10px;
    background: var(--crimson);
  }
  .wordmark {
    position: absolute;
    left: 248px;
    top: 50px;
    font-weight: 900;
    font-size: 31px;
    line-height: 1.08;
    color: var(--ink);
    letter-spacing: 0.5px;
    display: flex;
    align-items: center;
    gap: 10px;
  }
  .wordmark-square {
    width: 14px; height: 14px;
    background: var(--crimson);
    flex: none;
  }
  .person {
    position: absolute;
    left: 248px;
    top: 166px;
  }
  .person-name {
    font-size: 18px;
    font-weight: 400;
    color: var(--ink);
    letter-spacing: 0.3px;
  }
  .person-role {
    font-size: 13px;
    color: var(--crimson);
    margin-top: -1px;
  }
  .contact-list {
    position: absolute;
    left: 248px;
    top: 211px;
    list-style: none;
    font-size: 13px;
    color: var(--ink);
  }
  .contact-list li {
    display: flex;
    align-items: center;
    gap: 6px;
    height: 17px;
  }
  .contact-icon { width: 12px; height: 12px; fill: var(--crimson); flex: none; }

  .back-wordmark {
    position: absolute;
    left: 336px;
    top: 129px;
    font-weight: 900;
    font-size: 15px;
    line-height: 1.15;
    color: #ffffff;
    display: flex;
    align-items: center;
    gap: 6px;
  }
  .back-wordmark .wordmark-square { width: 8px; height: 8px; }
</style>
</head>
<body>
  <section class="card card-front">
    <div class="portrait" role="img" aria-label="Portrait photo of the managing director in a dark blazer"></div>
    <div class="wordmark">
      <span>VENTURE<br>KELO</span>
      <span class="wordmark-square"></span>
    </div>
    <div class="person">
      <p class="person-name">DAMIÁN ORTALVE</p>
      <p class="person-role">Managing Director</p>
    </div>
    <ul class="contact-list">
      <li>
        <svg class="contact-icon" viewBox="0 0 24 24" aria-hidden="true"><path d="M3 8c0-3 4-5 9-5s9 2 9 5v2h-5V8H8v2H3zM6 11h12l2 9H4zM12 13a3 3 0 1 0 0 6 3 3 0 0 0 0-6z"/></svg>
        <span>044-000 318 275</span>
      </li>
      <li>
        <svg class="contact-icon" viewBox="0 0 24 24" aria-hidden="true"><path d="M2 5h20v14H2zM4 7v.5l8 6 8-6V7zM4 10v7h16v-7l-8 6z"/></svg>
        <span>info@kelo-example.pe</span>
      </li>
    </ul>
    <div class="brand-band"></div>
  </section>

  <section class="card card-back">
    <div class="back-wordmark">
      <span>VENTURE<br>KELO</span>
      <span class="wordmark-square"></span>
    </div>
  </section>
</body>
</html>
```